Website Upgrade

Create new look for existing website: www.lunarisgrove.ca . You will find details on what we are about on the website. Email us at lunaris.grove@mailbright.ca if you have any questions. We will be more than happy to answer.
Lunaris grove is a website for women focused on empowering women.
Website must:
1. Be able to stream videos
2. Use of blogs
3. Purple must be one of the colours used in the scheme.
4. Must use existing lunaris grove logo (purple head with 'Lunaris Grove' script in white.. see on homepage). However, we are open to new logo suggestions
5. Must be professional. We are trendy but not boring.

```html
<!DOCTYPE html>
<html lang="en">
<head>
<meta charset="utf-8">
<title>Lunaris Grove</title>
<link href="https://fonts.googleapis.com/css2?family=Open+Sans:wght@400;600;700&family=Oswald:wght@400;500&display=swap" rel="stylesheet">
<style>
:root{
  --purple:#7b2d8e;
  --purple-soft:#a24bb3;
  --pink:#e0307a;
  --orange:#f7941d;
  --ink:#222225;
  --dark:#1b1b1d;
  --grey:#77777c;
  --line:#dcdcdf;
  --white:#ffffff;
}
*{margin:0;padding:0;box-sizing:border-box}
html,body{width:865px;height:1200px;overflow:hidden;background:var(--white)}
body{font-family:"Open Sans",sans-serif;color:var(--ink);font-size:9px;line-height:1.45}
.container{width:540px;margin:0 auto;position:relative}

.topbar{height:18px;background:var(--dark);display:flex;align-items:center;justify-content:center;position:relative}
.topbar nav{display:flex;gap:16px}
.topbar nav a{color:#cfcfd3;font-size:6.5px;letter-spacing:.6px;text-decoration:none;text-transform:uppercase}
.topbar nav a.active{color:var(--pink)}
.topbar .social{position:absolute;right:20px;top:5px;display:flex;gap:5px}
.dot{width:8px;height:8px;border-radius:50%;background:#55555a;display:block}

.masthead{height:77px;display:flex;align-items:center;justify-content:center;gap:9px}
.brand-mark{width:24px;height:24px;border-radius:50%;background:var(--purple)}
.brand-name{font-weight:600;font-size:24px;color:var(--purple);letter-spacing:.4px}

.hero{height:207px;position:relative;background:linear-gradient(180deg,#d3d1d6 0%,#aaa6ae 55%,#8e8a93 100%)}
.hero-card{position:absolute;left:50%;top:62px;transform:translateX(-50%);width:280px;background:rgba(255,255,255,.93);text-align:center;padding:12px 10px 11px}
.hero-card .lead{font-size:13px;color:#444}
.hero-card .power{font-size:23px;color:var(--purple);line-height:1.15}
.hero-card .power b{font-weight:700;color:var(--pink)}
.btn{display:inline-block;background:var(--pink);color:var(--white);font-size:6.5px;font-weight:700;letter-spacing:.6px;padding:5px 12px;border-radius:2px;text-transform:uppercase}
.hero-card .btn{margin-top:7px}
.hero-arrow{position:absolute;top:90px;width:18px;height:26px;background:rgba(0,0,0,.35);display:flex;align-items:center;justify-content:center}
.hero-arrow.prev{left:0}.hero-arrow.next{right:0}

.info{height:58px}
.info .container{display:flex;align-items:center;height:58px}
.phone{font-family:"Oswald",sans-serif;font-size:25px;font-weight:400;width:195px;letter-spacing:.5px}
.address{font-size:6.5px;color:var(--grey);line-height:1.7}
.address div{display:flex;align-items:center;gap:5px}
.account{position:absolute;right:0;top:12px;display:flex}
.account span{font-size:6.5px;font-weight:700;color:var(--white);padding:4px 10px;text-transform:uppercase}
.account .login{background:var(--purple)}
.account .register{background:var(--ink)}

.feature{height:150px}
.feature .container{display:flex;height:150px}
.tiles{width:250px;display:grid;grid-template-columns:repeat(3,1fr);grid-template-rows:1fr 1fr;gap:2px}
.tile{background:linear-gradient(135deg,#6d5a58,#b39a8c)}
.tile.b{background:linear-gradient(135deg,#3a3a3f,#8a7f7a)}
.tile.c{background:linear-gradient(135deg,#c9a68a,#7d5d4e)}
.tile.accent{background:var(--purple);color:var(--white);font-size:6px;font-weight:700;display:flex;align-items:flex-end;padding:5px;text-transform:uppercase}
.promo{width:120px;background:var(--orange);color:var(--white);padding:12px 10px;position:relative}
.promo h2{font-family:"Oswald",sans-serif;font-weight:500;font-size:18px;line-height:1.05;text-transform:uppercase}
.promo p{font-size:6.5px;margin-top:7px;line-height:1.55}
.promo .go{position:absolute;right:0;bottom:0;width:18px;height:18px;background:var(--purple);display:flex;align-items:center;justify-content:center}
.intro{flex:1;padding:6px 0 0 12px}
.intro h3{font-family:"Oswald",sans-serif;font-weight:400;color:var(--purple);font-size:14px;line-height:1.15;text-transform:uppercase}
.intro p{font-size:6.5px;color:var(--grey);margin-top:7px;line-height:1.65}

.columns{height:355px}
.columns .container{display:flex;gap:18px;padding-top:12px}
.col{flex:1;min-width:0}
.col h4{font-family:"Oswald",sans-serif;font-weight:500;font-size:12px;text-transform:uppercase;padding-bottom:4px;border-bottom:1px solid var(--line);position:relative;margin-bottom:9px}
.col h4::after{content:"";position:absolute;left:0;bottom:-1px;width:30px;height:2px;background:var(--purple)}
.col .photo{width:100%;height:120px;background:linear-gradient(160deg,#4a4a4e,#9a9aa0)}
.col .photo.warm{background:linear-gradient(160deg,#e0b79a,#a97462)}
.col p{font-size:6.5px;color:var(--grey);line-height:1.65;margin-top:5px}
.name{font-family:"Oswald",sans-serif;color:var(--purple);font-size:10px;text-transform:uppercase;margin-top:7px}
.caps{font-size:7px;font-weight:700;color:var(--ink);text-transform:uppercase;line-height:1.5;margin-top:7px}
.more{display:block;font-size:6px;font-weight:700;color:var(--pink);text-transform:uppercase;margin-top:9px;letter-spacing:.4px}
.faq dt{font-size:7px;font-weight:700;color:var(--purple);margin-top:6px}
.faq dd{font-size:6.5px;color:var(--grey);padding-bottom:5px;border-bottom:1px solid var(--line);line-height:1.6}

.contact{height:215px;position:relative;background:linear-gradient(180deg,#3a3540 0%,#1e1d21 40%,#2b2830 72%,#161518 100%)}
.contact h4{color:var(--white);text-align:center;font-family:"Oswald",sans-serif;font-weight:500;font-size:14px;padding-top:30px;text-transform:uppercase}
.contact h4::after{content:"";display:block;width:30px;height:2px;background:var(--purple-soft);margin:5px auto 0}
.form{width:520px;margin:14px auto 0}
.row{display:flex;gap:10px}
.field{flex:1;height:22px;background:rgba(255,255,255,.1);border:1px solid rgba(255,255,255,.2);color:#bbb;font-size:6.5px;padding:6px 8px}
.field.msg{height:72px;margin-top:9px}
.send{display:flex;justify-content:flex-end;margin-top:9px}

.footer{height:120px;text-align:center;padding-top:26px}
.footer nav{display:flex;justify-content:center;gap:10px}
.footer nav a{font-size:6.5px;color:var(--grey);text-decoration:none;text-transform:uppercase}
.footer .copy{font-size:6.5px;color:var(--grey);margin-top:4px}
.footer .social{display:flex;justify-content:center;gap:6px;margin-top:8px}
.footer .dot{background:var(--purple-soft)}
</style>
</head>
<body>

<header>
  <div class="topbar">
    <nav>
      <a class="active" href="#">Home</a><a href="#">Lunaris Grove</a><a href="#">FAQ</a><a href="#">Our Blogs</a><a href="#">Contact</a>
    </nav>
    <div class="social"><span class="dot"></span><span class="dot"></span><span class="dot"></span><span class="dot"></span></div>
  </div>
  <div class="masthead">
    <span class="brand-mark"></span>
    <span class="brand-name">Lunaris Grove</span>
  </div>
</header>

<section class="hero" role="img" aria-label="Photo of women with raised arms celebrating outdoors">
  <div class="hero-arrow prev"><svg width="8" height="10" viewBox="0 0 8 10"><path d="M6 1 2 5l4 4" stroke="#fff" stroke-width="1.6" fill="none"/></svg></div>
  <div class="hero-card">
    <div class="lead">Embody your radiance, magnetism, and</div>
    <div class="power">feminine power <b>NOW</b></div>
    <span class="btn">Watch Video Now</span>
  </div>
  <div class="hero-arrow next"><svg width="8" height="10" viewBox="0 0 8 10"><path d="M2 1l4 4-4 4" stroke="#fff" stroke-width="1.6" fill="none"/></svg></div>
</section>

<section class="info">
  <div class="container">
    <div class="phone">+49 301 55820</div>
    <div class="address">
      <div><svg width="6" height="8" viewBox="0 0 6 8"><path d="M3 0a3 3 0 0 0-3 3c0 2 3 5 3 5s3-3 3-5a3 3 0 0 0-3-3z" fill="#7b2d8e"/></svg>Lindenhof Allee 14, 10115 Berlin</div>
      <div><svg width="6" height="8" viewBox="0 0 6 8"><path d="M3 0a3 3 0 0 0-3 3c0 2 3 5 3 5s3-3 3-5a3 3 0 0 0-3-3z" fill="#7b2d8e"/></svg>Germany</div>
      <div><svg width="7" height="6" viewBox="0 0 7 6"><rect x=".5" y=".5" width="6" height="5" fill="none" stroke="#7b2d8e"/><path d="M.5.5 3.5 3l3-2.5" stroke="#7b2d8e" fill="none"/></svg>lunaris.grove@mailbright.ca</div>
    </div>
    <div class="account"><span class="login">Login</span><span class="register">Register</span></div>
  </div>
</section>

<section class="feature">
  <div class="container">
    <div class="tiles">
      <div class="tile" role="img" aria-label="Woman portrait photo"></div>
      <div class="tile c" role="img" aria-label="Woman in nature photo"></div>
      <div class="tile b" role="img" aria-label="Woman dancing photo"></div>
      <div class="tile b" role="img" aria-label="Woman silhouette photo"></div>
      <div class="tile accent">Self Confidence</div>
      <div class="tile c" role="img" aria-label="Woman smiling photo"></div>
    </div>
    <div class="promo">
      <h2>Lunaris<br>Grove</h2>
      <p>Discover your true feminine nature and live with grace and joy.</p>
      <span class="go"><svg width="6" height="8" viewBox="0 0 6 8"><path d="M1 1l4 3-4 3" stroke="#fff" stroke-width="1.4" fill="none"/></svg></span>
    </div>
    <div class="intro">
      <h3>Self confidence, love, awakening, and trust</h3>
      <p>In today's world many women have no knowledge of their inner strength. We guide each woman to reconnect with her body, her voice and her heart, so she can live fully and love freely.</p>
    </div>
  </div>
</section>

<section class="columns">
  <div class="container">
    <div class="col">
      <h4>What We Believe</h4>
      <div class="photo" role="img" aria-label="Photo of a woman in soft light"></div>
      <div class="caps">Every woman holds a quiet power within her heart.</div>
      <p>We believe that true beauty grows from self love, trust and presence in the body.</p>
      <span class="more">Read More</span>
    </div>
    <div class="col">
      <h4>FAQs</h4>
      <dl class="faq">
        <dt>What is Lunaris Grove?</dt>
        <dd>A path for women to awaken their inner radiance.</dd>
        <dt>Who is it for?</dt>
        <dd>Any woman ready to grow in confidence and joy.</dd>
        <dt>How can it help me?</dt>
        <dd>It brings calm, strength and deeper connection.</dd>
        <dt>How do you be powerful and feminine?</dt>
        <dd>By trusting your body and your own true voice.</dd>
        <dt>Is this for you?</dt>
        <dd>If you long for more ease, then yes it is.</dd>
      </dl>
      <span class="more">Read More</span>
    </div>
    <div class="col">
      <h4>Our Blogs</h4>
      <div class="photo warm" role="img" aria-label="Portrait photo of the blog author"></div>
      <div class="name">Lena Varga</div>
      <p>Lena is a licensed teacher of Lunaris Grove who helps women find their natural grace and power.</p>
      <span class="more">Read More</span>
    </div>
  </div>
</section>

<section class="contact" role="img" aria-label="Dark photo of a woman standing in a misty landscape">
  <h4>Contact Us</h4>
  <div class="form">
    <div class="row">
      <div class="field">Name*</div>
      <div class="field">Email Address*</div>
      <div class="field">Subject*</div>
    </div>
    <div class="field msg">Message*</div>
    <div class="send"><span class="btn">Send</span></div>
  </div>
</section>

<footer class="footer">
  <nav><a href="#">Home</a><a href="#">Lunaris Grove</a><a href="#">FAQ</a><a href="#">Our Blogs</a><a href="#">Contact Us</a></nav>
  <div class="copy">© 2024 Lunaris Grove. All rights reserved. | www.lunarisgrove.ca</div>
  <div class="social"><span class="dot"></span><span class="dot"></span><span class="dot"></span><span class="dot"></span></div>
</footer>

</body>
</html>
```